Recently launched Investment banking and Corporate Advisory firm focused and experienced on Selling

We are looking for a dynamic Brochure that can highlight our areas of focus, experience and expertise.
We have a small but seasoned team of professionals in the organisation and want to showcase our ability to provide Growth and / or exit solutions for our clients.
We are a boutique firm and want to focus on showcasing the fact that we strive for excellence and quality and not quantity.

Our core business avtivity at this time is Sell Side M&A services (this means that we sell private businesses). We are unique in our approach to "partnering businesses" with other companies...not just selling them. We focus more on the "strategic fit" of the potential partner rather than the simple valuation that a potential partner (buyer) would place on the company.

We have really been focusing on "GROWTH and EXIT" strategies for private business owners. Customers usually talk to us for 1 of two main reasons. Their businesses are usually very stable or rapidly growing , often to a point where the owners are no longer comfortable running them on their own. They often need capital for expansion or a team to help them expand their business into other countries and markets. for this we look for a solution for them and often it is finding them a strategic partner who will want to buy the majority of the business. There are also the clients that are looking for an exit strategy (typically they are older and getting ready to retire) they are typically seeking for a way to exit the business (sell the business).

A tagline I often use is "Customer Vision" - We see our customers business and needs through their eyes.

Our company website is www.keldmoorpartners.com and is a work in progress

Target Market(s)

Business Owners (CEO / Presidents)
Mostly Male
Late 40's to late 60's
Very often they will be Engineers
Very Successful and hard working
Many of them looking for GROWTH solutions
Many of them looking for Retirement
We heavily focus on Oil and Gas Service companies, Oil and Gas manufacturing / oilfield services / Technology Companies and Industrial Companies

Industry/Entity Type

Boutique

Font styles to use
Sans Serif

Colors
f37022
33a6d7

Requirements
Must have
• This must be extremely high quality. The people that will receive these brochures are Presidents and CEO's of companies. Every document we give the customer directly reflects the quality of service we will provide for them.
Nice to have
• Pictures tell a great story and can also tell about the areas of experience and expertise that we have

Ideally we'd be interested in a square shaped marketing document (signifies strength and solidness in the business/opportunity) - either 5x5 or 7x7 size in a 4-6 page (double-sided) saddle-stitched booklet.
We'd like to relay an emotion while also describing our business.

```html
<!DOCTYPE html>
<html lang="en">
<head>
<meta charset="utf-8">
<title>Keld Moor Partners – Merger and Acquisition Advisory Services</title>
<link rel="stylesheet" href="https://fonts.googleapis.com/css2?family=Questrial&family=Didact+Gothic&display=swap">
<style>
  :root {
    --blue: #1b7bc4;
    --blue-text: #1f78c1;
    --orange: #f06a1e;
    --tab-text: #ffc7a0;
    --tab-rule: #f7a77a;
    --paper: #f7f7f8;
    --body-text: #2b6fb0;
    --backdrop: #e6e6e6;
  }
  * { box-sizing: border-box; margin: 0; padding: 0; }
  html, body { width: 1200px; height: 908px; overflow: hidden; }
  body {
    background: var(--backdrop);
    font-family: "Didact Gothic", sans-serif;
    position: relative;
  }
  .spread {
    position: absolute;
    left: 80px; top: 74px;
    width: 1040px; height: 760px;
    display: flex;
    box-shadow: 0 6px 24px rgba(0,0,0,.18);
  }
  .page {
    position: relative;
    width: 520px; height: 760px;
    background: var(--paper);
    display: flex;
  }
  .page--left .content { border-right: 1px solid #dcdcdc; }

  .content {
    position: relative;
    flex: 1;
    display: flex;
    flex-direction: column;
  }
  .page-title {
    font-family: "Questrial", sans-serif;
    font-weight: 400;
    color: var(--blue-text);
    font-size: 21px;
    white-space: nowrap;
    text-align: center;
    margin-top: 84px;
    letter-spacing: -.2px;
  }
  .section-title {
    font-family: "Questrial", sans-serif;
    font-weight: 400;
    color: var(--blue-text);
    font-size: 13px;
    text-align: center;
    margin-top: 78px;
  }
  .columns {
    display: grid;
    grid-template-columns: 1fr 1fr;
    margin: 16px 20px 0 24px;
    height: 420px;
  }
  .column { padding: 36px 14px 0 0; font-size: 10.5px; line-height: 1.36; color: var(--body-text); }
  .column + .column { border-left: 1.5px solid var(--blue); padding-left: 16px; padding-right: 0; }
  .column-label { margin-bottom: 14px; }
  .column-intro { margin-bottom: 40px; }
  .service-list { list-style: none; }
  .service-list li { padding-left: 10px; }
  .service-list li::before { content: "*"; }
  .bottom-band {
    position: absolute; left: 0; right: 0; bottom: 0;
    height: 96px;
    background: var(--blue);
  }

  .tab-rail {
    width: 96px;
    display: flex;
    flex-direction: column;
    background: var(--orange);
  }
  .tab {
    flex: 1;
    display: flex;
    align-items: center;
    justify-content: flex-end;
    padding: 0 5px;
    font-family: "Questrial", sans-serif;
    font-size: 13.5px;
    line-height: 1.25;
    color: var(--tab-text);
    text-align: right;
    border-top: 2px solid var(--tab-rule);
  }
  .tab--long { font-size: 11.5px; letter-spacing: -.2px; }
  .page--left .tab { justify-content: flex-start; text-align: left; }
  .tab--active {
    flex: 0 0 102px;
    position: relative;
    border-top: none;
    color: #fff;
    background: var(--blue);
  }
  .tab--active .tab-notch {
    position: absolute; top: 0; height: 102px; width: 22px;
  }
  .page--right .tab--active .tab-notch { left: -22px; }
  .page--left .tab--active .tab-notch { right: -22px; }
  .tab-label { position: relative; z-index: 1; }
</style>
</head>
<body>
<main class="spread">

  <section class="page page--left" aria-label="Left page">
    <nav class="tab-rail">
      <div class="tab tab--active">
        <svg class="tab-notch" viewBox="0 0 22 102" preserveAspectRatio="none" aria-hidden="true"><polygon points="0,0 8,0 22,51 8,102 0,102" fill="#1b7bc4"/></svg>
        <span class="tab-label">Mergers &amp;<br>Acquisitions</span>
      </div>
      <div class="tab">Risk<br>Management</div>
      <div class="tab">Business<br>Development<br>Solution</div>
      <div class="tab">Growth<br>Solution</div>
      <div class="tab">Exit<br>Strategies</div>
      <div class="tab">Sales &amp;<br>Marketing<br>Solution</div>
      <div class="tab tab--long">Communications<br>Solution</div>
      <div class="tab">Outsourced<br>Solution</div>
      <div class="tab">Special<br>Projects<br>Solution</div>
    </nav>
    <div class="content">
      <h1 class="page-title">Merger and Acquisition Advisory Services</h1>
      <h2 class="section-title">Merger &amp; Acquisition Advisory</h2>
      <div class="columns">
        <div class="column">
          <p class="column-label">-Buy Side-</p>
          <p class="column-intro">If you want to expand your business in a specific geographic area or industry we will help you target potential acquisitions, negotiate a deal and complete your diligence.</p>
          <p>Our services include:</p>
          <ul class="service-list">
            <li>Synergy business plans</li><li>Recast financial</li><li>Brief writing and generation</li><li>Extensive research</li><li>Business intelligence reports</li><li>Market studies/reports</li><li>Feasibility studies</li><li>Coaching and mentoring</li><li>Contract negotiations</li><li>Due diligence facilitation</li><li>Project management</li>
          </ul>
        </div>
        <div class="column">
          <p class="column-label">-Sell Side-</p>
          <p class="column-intro">After a health check on the viability of going to market, Keld Moor Partners will use proven systems to assist you in taking your business to market and maximizing the value of your company.</p>
          <p>We provide:</p>
          <ul class="service-list">
            <li>Synergy business plans</li><li>Recast financial</li><li>Financial business plans</li><li>Extensive research</li><li>Prospectus/Information memorandum writing and generation</li><li>Detailed research lists</li><li>Coaching and mentoring</li><li>Contract negotiations</li><li>Due diligence facilitation</li><li>Outbound prospect generation</li><li>Project management</li>
          </ul>
        </div>
      </div>
      <div class="bottom-band"></div>
    </div>
  </section>

  <section class="page page--right" aria-label="Right page">
    <div class="content">
      <h1 class="page-title">Merger and Acquisition Advisory Services</h1>
      <h2 class="section-title">Merger &amp; Acquisition Advisory</h2>
      <div class="columns">
        <div class="column">
          <p class="column-label">-Buy Side-</p>
          <p class="column-intro">If you want to expand your business in a specific geographic area or industry we will help you target potential acquisitions, negotiate a deal and complete your diligence.</p>
          <p>Our services include:</p>
          <ul class="service-list">
            <li>Synergy business plans</li><li>Recast financial</li><li>Brief writing and generation</li><li>Extensive research</li><li>Business intelligence reports</li><li>Market studies/reports</li><li>Feasibility studies</li><li>Coaching and mentoring</li><li>Contract negotiations</li><li>Due diligence facilitation</li><li>Project management</li>
          </ul>
        </div>
        <div class="column">
          <p class="column-label">-Sell Side-</p>
          <p class="column-intro">After a health check on the viability of going to market, Keld Moor Partners will use proven systems to assist you in taking your business to market and maximizing the value of your company.</p>
          <p>We provide:</p>
          <ul class="service-list">
            <li>Synergy business plans</li><li>Recast financial</li><li>Financial business plans</li><li>Extensive research</li><li>Prospectus/Information memorandum writing and generation</li><li>Detailed research lists</li><li>Coaching and mentoring</li><li>Contract negotiations</li><li>Due diligence facilitation</li><li>Outbound prospect generation</li><li>Project management</li>
          </ul>
        </div>
      </div>
      <div class="bottom-band"></div>
    </div>
    <nav class="tab-rail">
      <div class="tab tab--active">
        <svg class="tab-notch" viewBox="0 0 22 102" preserveAspectRatio="none" aria-hidden="true"><polygon points="22,0 14,0 0,51 14,102 22,102" fill="#1b7bc4"/></svg>
        <span class="tab-label">Mergers &amp;<br>Acquisitions</span>
      </div>
      <div class="tab">Risk<br>Management</div>
      <div class="tab">Business<br>Development<br>Solution</div>
      <div class="tab">Growth<br>Solution</div>
      <div class="tab">Exit<br>Strategies</div>
      <div class="tab">Sales &amp;<br>Marketing<br>Solution</div>
      <div class="tab tab--long">Communications<br>Solution</div>
      <div class="tab">Outsourced<br>Solution</div>
      <div class="tab">Special<br>Projects<br>Solution</div>
    </nav>
  </section>

</main>
</body>
</html>
```